I need a direct mail postcard made up for my marketing campaign

I am starting a marketing campaign and need a design for a post card. I own an iron door company and need to have before and after images on the post card to showcase what our work looks like. I have provided pictures to use below.

The design needs to be two sided. The logo should be on the front.

The tag line for this campaign is: Design the smile your home deserves.

Words to also use: Distinctive style, Work of Art, One-of-a-Kind, Elegant, Modern, Innovative, Unique

My information for the card
Name: Dean Harlowe
Phone number: (555)-318-2764
Email: Dean@wroughtgatestudio.example

The US postal system is very picky as to what can be sent in the mail. The only requirement they have is for the address. There needs to be a 2inch (50.8mm) by 4inch (101.6mm) blank space on the bottom right hand corner on the back of the card.

Target Market(s)

Home owners

Industry/Entity Type

Home Improvement

Font styles to use
Serif
Decorative

Colors
0555a3
ffffff
ec1f27

Requirements
Must have
• My logo, My contact information, before and after pictures
• Provided 3D images
Nice to have
• Words that describe iron doors
• A contrast between contemporary and ornate doors.

```html
<!DOCTYPE html>
<html lang="en">
<head>
<meta charset="utf-8">
<title>Wroughtgate Studio – Direct Mail Postcard</title>
<link href="https://fonts.googleapis.com/css2?family=Tinos:wght@400;700&family=Yellowtail&display=swap" rel="stylesheet">
<style>
  :root {
    --brand-blue: #0555a3;
    --brand-red: #ec1f27;
    --deep-navy: #0a2a6b;
    --deep-red: #9a1218;
    --white: #ffffff;
    --paper: #ececec;
    --stage: #3a3a3a;
    --wood: #6a3a1c;
    --wood-dark: #4a2410;
  }
  * { box-sizing: border-box; margin: 0; padding: 0; }
  html, body { width: 1200px; height: 1200px; overflow: hidden; }
  body { background: var(--stage); position: relative; font-family: "Tinos", serif; }

  .postcard { position: absolute; width: 714px; height: 462px; overflow: hidden; }
  .postcard--front { left: 128px; top: 102px; background: var(--paper); }
  .postcard--back  { left: 346px; top: 616px;
    background: linear-gradient(90deg, var(--brand-blue) 0%, #8ea3d4 22%, #e6e9f4 50%, var(--white) 68%); }

  .shape-layer { position: absolute; inset: 0; width: 100%; height: 100%; }

  /* front */
  .brand { position: absolute; left: 22px; top: 40px; width: 160px; display: flex; align-items: center; gap: 8px; color: var(--white); }
  .brand__dot { width: 14px; height: 14px; border-radius: 50%; background: var(--white); flex: none; }
  .brand__name { font-family: "Tinos", serif; font-weight: 700; font-size: 17px; line-height: 1.1; }
  .tagline { position: absolute; left: 208px; top: 30px; width: 480px; text-align: center;
    font-family: "Yellowtail", cursive; font-weight: 400; font-size: 30px; line-height: 1.2;
    color: var(--white); white-space: nowrap; }

  .qualities { position: absolute; left: 38px; top: 140px; list-style: none; }
  .qualities li { font-weight: 700; font-size: 24px; line-height: 29.5px; display: flex; align-items: center; gap: 8px; }
  .qualities li::before { content: ""; width: 0; height: 0; border-top: 5px solid transparent; border-bottom: 5px solid transparent; border-left: 10px solid currentColor; }
  .qualities .blue { color: var(--brand-blue); }
  .qualities .red { color: var(--brand-red); }

  .door { position: absolute; background: linear-gradient(180deg, var(--wood) 0%, var(--wood-dark) 100%); border-radius: 2px; }
  .door--ornate { left: 282px; top: 118px; width: 182px; height: 244px; }
  .door--modern { left: 510px; top: 118px; width: 148px; height: 244px; }

  .portrait { position: absolute; border-radius: 50%; border: 3px solid var(--white); background: radial-gradient(circle at 50% 40%, #c9a88c, #5a5f6a); }
  .postcard--front .portrait { left: 37px; top: 350px; width: 96px; height: 96px; }

  .front-contact { position: absolute; left: 147px; top: 412px; display: flex; align-items: baseline; gap: 16px; color: var(--white); font-weight: 700; white-space: nowrap; }
  .front-contact .name { font-size: 22px; }
  .front-contact .detail { font-size: 14px; display: flex; align-items: center; gap: 5px; }
  .icon { width: 14px; height: 14px; fill: currentColor; flex: none; }

  /* back */
  .tab { position: absolute; top: 0; height: 40px; width: 155px; color: var(--white); font-weight: 700; font-size: 15px; padding-top: 14px; }
  .tab--before { background: var(--brand-red); padding-left: 38px; }
  .tab--after { background: var(--brand-blue); text-align: right; padding-right: 34px; }

  .shot { position: absolute; }
  .shot--before-1 { left: 37px; top: 60px; width: 73px; height: 150px; background: linear-gradient(180deg, #7a3418, #5a2410); }
  .shot--after-1 { left: 186px; top: 60px; width: 103px; height: 150px; background: linear-gradient(180deg, #2a2a30, #6b5a2c 50%, #1e1e22); }
  .shot--before-2 { left: 350px; top: 60px; width: 63px; height: 150px; background: linear-gradient(180deg, #8a6a2a 0%, #f2f2f2 22%, #e4e4e4 100%); }
  .shot--after-2 { left: 514px; top: 60px; width: 84px; height: 150px; border-radius: 42px 42px 0 0; background: linear-gradient(180deg, #3a3a55, #4a4a66); }

  .postcard--back .portrait { left: 43px; top: 232px; width: 84px; height: 84px; }
  .back-name { position: absolute; left: 186px; top: 266px; font-size: 24px; font-weight: 700; color: var(--brand-blue); white-space: nowrap; }
  .back-details { position: absolute; left: 44px; top: 326px; color: var(--white); font-weight: 700; font-size: 19px; line-height: 25px; }
  .back-details div { display: flex; align-items: center; gap: 10px; white-space: nowrap; }
  .back-details .icon { width: 18px; height: 18px; }
</style>
</head>
<body>

<section class="postcard postcard--front" aria-label="Postcard front">
  <svg class="shape-layer" viewBox="0 0 714 462" preserveAspectRatio="none" aria-hidden="true">
    <path d="M0 0 H714 V95 H215 C190 95 185 130 150 130 H0 Z" fill="var(--brand-blue)"/>
    <path d="M215 95 H714 V100 H218 C195 100 188 136 150 136 H0 V130 H150 C185 130 190 95 215 95 Z" fill="var(--deep-navy)"/>
    <path d="M0 360 H150 C185 360 195 394 230 394 H714 V462 H0 Z" fill="var(--brand-red)"/>
    <path d="M0 355 H150 C185 355 195 389 230 389 H714 V394 H230 C195 394 185 360 150 360 H0 Z" fill="var(--deep-red)"/>
  </svg>

  <div class="brand"><span class="brand__dot"></span><span class="brand__name">Wroughtgate Studio</span></div>
  <h1 class="tagline">Design the Smile Your Home Deserves</h1>

  <ul class="qualities">
    <li class="blue">Distinctive style</li>
    <li class="red">Work of Art</li>
    <li class="blue">One-of-a-Kind</li>
    <li class="red">Elegant</li>
    <li class="blue">Modern</li>
    <li class="red">Innovative</li>
    <li class="blue">Unique</li>
  </ul>

  <div class="door door--ornate" role="img" aria-label="3D rendering of an ornate wooden double door with sweeping curved ironwork"></div>
  <div class="door door--modern" role="img" aria-label="3D rendering of a contemporary door with horizontal glass slots and sidelights"></div>

  <div class="portrait" role="img" aria-label="Portrait photo of Dean Harlowe"></div>
  <div class="front-contact">
    <span class="name">Dean Harlowe</span>
    <span class="detail"><svg class="icon" viewBox="0 0 24 24"><path d="M6.6 10.8a15.1 15.1 0 0 0 6.6 6.6l2.2-2.2a1 1 0 0 1 1-.25 11.4 11.4 0 0 0 3.6.57 1 1 0 0 1 1 1V20a1 1 0 0 1-1 1A17 17 0 0 1 3 4a1 1 0 0 1 1-1h3.5a1 1 0 0 1 1 1c0 1.25.2 2.45.57 3.57a1 1 0 0 1-.25 1z"/></svg>(555)-318-2764</span>
    <span class="detail"><svg class="icon" viewBox="0 0 24 24"><path d="M2 5h20v14H2z M2 5l10 8 10-8" fill="currentColor" stroke="var(--brand-red)" stroke-width="1.5"/></svg>Dean@wroughtgatestudio.example</span>
  </div>
</section>

<section class="postcard postcard--back" aria-label="Postcard back">
  <div class="tab tab--before" style="left:0">BEFORE</div>
  <div class="tab tab--after" style="left:155px">AFTER</div>
  <div class="tab tab--before" style="left:309px">BEFORE</div>
  <div class="tab tab--after" style="left:463px">AFTER</div>

  <div class="shot shot--before-1" role="img" aria-label="Before photo: worn wooden double entry door"></div>
  <div class="shot shot--after-1" role="img" aria-label="After photo: black iron double door with scrollwork and glass"></div>
  <div class="shot shot--before-2" role="img" aria-label="Before photo: plain white paneled double door"></div>
  <div class="shot shot--after-2" role="img" aria-label="After photo: arched dark iron double door with wreaths"></div>

  <svg class="shape-layer" viewBox="0 0 712 462" preserveAspectRatio="none" aria-hidden="true">
    <path d="M0 270 H150 C180 270 190 302 225 302 H362 V386 H0 Z" fill="var(--brand-red)"/>
  </svg>

  <div class="portrait" role="img" aria-label="Portrait photo of Dean Harlowe"></div>
  <div class="back-name">Dean Harlowe</div>
  <div class="back-details">
    <div><svg class="icon" viewBox="0 0 24 24"><path d="M6.6 10.8a15.1 15.1 0 0 0 6.6 6.6l2.2-2.2a1 1 0 0 1 1-.25 11.4 11.4 0 0 0 3.6.57 1 1 0 0 1 1 1V20a1 1 0 0 1-1 1A17 17 0 0 1 3 4a1 1 0 0 1 1-1h3.5a1 1 0 0 1 1 1c0 1.25.2 2.45.57 3.570a1 1 0 0 1-.25 1z"/></svg>(555)-318-2764</div>
    <div><svg class="icon" viewBox="0 0 24 24"><path d="M2 5h20v14H2z M2 5l10 8 10-8" fill="currentColor" stroke="var(--brand-red)" stroke-width="1.5"/></svg>Dean@wroughtgatestudio.example</div>
  </div>
</section>

</body>
</html>
```